An innovative casting business is looking for a creative new packaging design. We create castings fo

We need a new creative packaging design for our creative castings. The packaging we used to have been similar to a tippy basket box with a handle. We used to use different materials (Wax) so it was very light and efficient. However now we are using stone so will need a brand new design and concept.
The final design should not be childish. We cater for all ages, it should be playful without being to over-sauced. We are looking for something creative and innovative and practical while also having a bit of a wow factor.

We do have a few ideas however would like to leave the door open. We are incredibly excited to see what everyone comes up with. By typing 'creative packaging' into google may bring some ideas...

Target Market(s)

Familes, Couples, Children, Keepsakes

Industry/Entity Type

Business

Requirements
Must have
• Must be innovative and creative.
Nice to have
• I would like to have the hand sit inside of something. This would be nice to have as it will stabilise the hand(s) for travel. I want to have something innovative and new. We have had the tippy basket type box before so would like to have something different. Its not important for it to have a handle.
Should not have
• Should not be childish

```html
<!DOCTYPE html>
<html lang="en">
<head>
<meta charset="utf-8">
<title>Casting Gift Box – Front Panel</title>
<link href="https://fonts.googleapis.com/css2?family=Marcellus&display=swap" rel="stylesheet">
<style>
  :root {
    --page-bg: #ececec;
    --box-black: #141414;
    --box-black-soft: #2a2a2b;
    --damask-tone: #3a3a3c;
    --window-red: #a01c1a;
    --window-red-mid: #8a1514;
    --window-red-dark: #5e0b0b;
    --cast-light: #eef0f0;
    --cast-mid: #c9cfd0;
    --silver-light: #f2f2f2;
    --silver-mid: #c4c4c4;
    --silver-dark: #8d8d8d;
    --text-light: #ffffff;
    --badge-text: #6b6b6b;
  }
  * { box-sizing: border-box; margin: 0; padding: 0; }
  html, body { width: 1200px; height: 1200px; overflow: hidden; }
  body {
    background: var(--page-bg);
    font-family: "Marcellus", serif;
    position: relative;
  }
  .box-handle {
    position: absolute;
    left: 214px;
    top: 68px;
    width: 772px;
    height: 210px;
  }
  .box-front {
    position: absolute;
    left: 214px;
    top: 276px;
    width: 772px;
    height: 774px;
    background: var(--box-black);
    overflow: hidden;
  }
  .box-front__damask {
    position: absolute;
    inset: 0;
    background:
      radial-gradient(ellipse 30% 12% at 20% 6%, rgba(70,70,72,0.55), transparent 70%),
      radial-gradient(ellipse 30% 12% at 55% 4%, rgba(70,70,72,0.5), transparent 70%),
      radial-gradient(ellipse 28% 12% at 88% 7%, rgba(70,70,72,0.55), transparent 70%),
      radial-gradient(ellipse 10% 30% at 4% 45%, rgba(60,60,62,0.45), transparent 70%),
      radial-gradient(ellipse 10% 30% at 96% 50%, rgba(60,60,62,0.45), transparent 70%),
      radial-gradient(ellipse 35% 10% at 40% 96%, rgba(60,60,62,0.45), transparent 70%),
      radial-gradient(ellipse 30% 10% at 80% 95%, rgba(60,60,62,0.4), transparent 70%),
      linear-gradient(180deg, var(--box-black-soft) 0%, var(--box-black) 30%, var(--box-black) 78%, var(--box-black-soft) 100%);
  }
  .box-slogan {
    position: absolute;
    top: 50px;
    left: 0;
    width: 100%;
    text-align: center;
    color: var(--text-light);
    font-size: 25px;
    letter-spacing: 0.5px;
  }
  .product-window {
    position: absolute;
    left: 98px;
    top: 98px;
    width: 576px;
    height: 580px;
    padding: 6px;
    background: linear-gradient(135deg, var(--silver-light), var(--silver-dark) 50%, var(--silver-light));
  }
  .product-window__scene {
    display: block;
    width: 564px;
    height: 568px;
  }
  .box-website {
    position: absolute;
    top: 720px;
    left: 0;
    width: 100%;
    text-align: center;
    color: var(--text-light);
    font-size: 20px;
    letter-spacing: 0.6px;
  }
  .brand-seal {
    position: absolute;
    left: 576px;
    top: 586px;
    width: 184px;
    height: 184px;
    border-radius: 50%;
    background: var(--box-black);
    display: flex;
    align-items: center;
    justify-content: center;
  }
  .brand-seal__disc {
    width: 154px;
    height: 154px;
    border-radius: 50%;
    background: radial-gradient(circle at 40% 35%, var(--silver-light) 0%, var(--silver-mid) 70%, var(--silver-dark) 100%);
    display: flex;
    align-items: center;
    justify-content: center;
  }
  .brand-seal__name {
    color: var(--badge-text);
    font-size: 20px;
    letter-spacing: 1px;
  }
</style>
</head>
<body>
  <svg class="box-handle" viewBox="0 0 772 210" aria-hidden="true">
    <defs>
      <linearGradient id="handleShade" x1="0" x2="1" y1="0" y2="0">
        <stop offset="0" stop-color="#0b0b0b"/>
        <stop offset="1" stop-color="#2e2e2f"/>
      </linearGradient>
    </defs>
    <path d="M56 28 Q56 0 84 0 L686 0 Q714 0 714 28 L714 150 L772 208 L0 208 L56 150 Z" fill="url(#handleShade)"/>
    <path d="M206 40 Q206 32 214 32 L556 32 Q564 32 564 40 L564 102 L206 102 Z" fill="#ffffff"/>
  </svg>

  <main class="box-front">
    <div class="box-front__damask" role="img" aria-label="Dark damask flourish pattern printed across the box"></div>
    <p class="box-slogan">Slogan Or Some Text Here</p>
    <div class="product-window">
      <svg class="product-window__scene" viewBox="0 0 564 568">
        <defs>
          <radialGradient id="nicheBack" cx="0.5" cy="0.3" r="0.8">
            <stop offset="0" stop-color="var(--window-red)"/>
            <stop offset="1" stop-color="var(--window-red-mid)"/>
          </radialGradient>
          <linearGradient id="nicheFloor" x1="0" x2="0" y1="0" y2="1">
            <stop offset="0" stop-color="#9a1716"/>
            <stop offset="1" stop-color="#b51f1c"/>
          </linearGradient>
          <radialGradient id="castTone" cx="0.5" cy="0.5" r="0.5">
            <stop offset="0" stop-color="var(--cast-light)"/>
            <stop offset="0.75" stop-color="var(--cast-mid)"/>
            <stop offset="1" stop-color="var(--cast-mid)" stop-opacity="0"/>
          </radialGradient>
        </defs>
        <rect width="564" height="568" fill="url(#nicheBack)"/>
        <polygon points="0,0 36,22 36,496 0,568" fill="var(--window-red-dark)" opacity="0.7"/>
        <polygon points="564,0 530,22 530,496 564,568" fill="var(--window-red-dark)" opacity="0.6"/>
        <polygon points="36,496 530,496 564,568 0,568" fill="url(#nicheFloor)"/>
        <line x1="20" y1="300" x2="250" y2="60" stroke="#ffffff" stroke-opacity="0.25" stroke-width="1"/>
        <line x1="26" y1="306" x2="256" y2="66" stroke="#ffffff" stroke-opacity="0.15" stroke-width="1"/>
        <line x1="380" y1="230" x2="530" y2="74" stroke="#ffffff" stroke-opacity="0.25" stroke-width="1"/>
        <line x1="386" y1="236" x2="536" y2="80" stroke="#ffffff" stroke-opacity="0.15" stroke-width="1"/>
        <ellipse cx="250" cy="320" rx="230" ry="255" fill="url(#castTone)" role="img" aria-label="Photo of a white stone casting of two clasped hands standing in the niche"/>
      </svg>
    </div>
    <p class="box-website">www.yourwebsite.com</p>
    <div class="brand-seal">
      <div class="brand-seal__disc">
        <span class="brand-seal__name">Keepstone</span>
      </div>
    </div>
  </main>
</body>
</html>
```